Wordpress Design Project for Medical clinic

I am a PODIATRY clinic: My current domain is www.brambleridgefootcare.com.au

I treat heel pain. ( Pain in the heel of the foot ) in Sydney, Australia

The majority of my patients are approximately 50 years of age, but some are younger and sporty. I treat runners, walkers, golfers and other sports such as boot camp.

My work is similar to that of a physiotherapist.

Target Market(s)

Industry/Entity Type

Clinic

Requirements
Must have
• My video on the home page ( autoplay )
My logo (i have a new logo which i will attach / share via dropbox)
Pictures
Sliders
information / content / contact details phone numbers
Nice to have
• Clinical feel / medical vibe

```html
<!DOCTYPE html>
<html lang="en">
<head>
<meta charset="utf-8">
<title>Brambleridge Foot Care</title>
<link href="https://fonts.googleapis.com/css2?family=Source+Sans+3:wght@300;400;600&display=swap" rel="stylesheet">
<style>
:root{
  --red:#d8202e;
  --red-light:#e84350;
  --nav:#e6313d;
  --ink:#1e1e1e;
  --grey:#6b6b6b;
  --line:#d9d9d9;
  --hero-bg:#f4f2f3;
  --footer:#333333;
  --white:#ffffff;
}
*{box-sizing:border-box;margin:0;padding:0}
html,body{width:1037px;height:1200px;overflow:hidden;background:var(--white);font-family:"Source Sans 3",sans-serif}
.page{position:relative;width:1037px;height:1200px;overflow:hidden}
.header{position:absolute;left:0;top:0;width:1037px;height:106px;background:linear-gradient(#e24552,var(--red))}
.brand{position:absolute;left:86px;top:22px;display:flex;align-items:center;gap:10px;color:var(--white);font-weight:600;font-size:30px;line-height:1}
.brand-mark{width:34px;height:34px;border-radius:50%;background:var(--white)}
.contact{position:absolute;right:101px;top:14px;text-align:right;color:var(--white)}
.contact .phone{font-size:25px;font-weight:400;line-height:1}
.contact .address{font-size:12px;font-weight:300;margin-top:2px}
.search{position:absolute;right:98px;top:67px;width:206px;height:26px;background:var(--white);border:1px solid #e9b4b8;border-radius:3px;font-size:10px;color:#888;padding:6px 10px}
.search svg{position:absolute;right:8px;top:5px}
.nav{position:absolute;left:0;top:106px;width:1037px;height:47px;background:var(--nav);display:flex;padding-left:73px}
.nav a{color:var(--white);text-decoration:none;font-size:17px;line-height:47px;padding:0 20px;border-right:1px solid #c5202c}
.nav a:last-child{border-right:none}
.hero{position:absolute;left:0;top:153px;width:1037px;height:344px;background:linear-gradient(#fff,var(--hero-bg));border-bottom:1px solid #b8b8b8}
.hero h1{position:absolute;left:90px;top:62px;font-weight:400;font-size:38px;line-height:44px;color:var(--ink)}
.hero h1 span{color:var(--red);display:block}
.hero p{position:absolute;left:90px;top:152px;width:390px;font-size:13px;line-height:21.5px;font-weight:300;color:var(--grey)}
.dots{position:absolute;left:94px;top:238px;display:flex;gap:3px}
.dots i{width:10px;height:10px;border-radius:50%;background:#bbb}
.dots i:first-child{background:#111}
.hero-photo{position:absolute;left:518px;top:41px;width:411px;height:263px;border:5px solid var(--white);border-radius:8px;box-shadow:0 0 3px rgba(0,0,0,.25);background:linear-gradient(135deg,#e8d0c2,#c89a86 55%,#3a3030)}
.card{position:absolute;top:518px;width:271px;height:282px;border:1px solid var(--line);border-radius:3px;background:var(--white)}
.card h2{height:46px;line-height:46px;padding-left:22px;font-weight:400;font-size:21px;color:var(--ink);background:linear-gradient(#fafafa,#ececec);border-bottom:1px solid var(--line)}
.card.is-active h2{color:var(--white);background:linear-gradient(var(--red-light),var(--red))}
.card .photo{position:absolute;left:16px;top:56px;width:240px;height:111px;border-radius:3px}
.card p{position:absolute;left:18px;top:179px;width:240px;font-size:11.5px;line-height:17px;font-weight:300;color:var(--grey)}
.card .more{position:absolute;left:19px;top:235px;font-size:12.5px;font-weight:600;color:var(--red);text-decoration:none}
.welcome h2{position:absolute;left:82px;top:838px;font-size:23px;font-weight:400;color:var(--red)}
.welcome p{position:absolute;left:82px;width:575px;font-size:11.5px;line-height:20.6px;font-weight:300;color:var(--grey)}
.video{position:absolute;left:673px;top:829px;width:270px;height:196px;border-radius:3px;background:linear-gradient(135deg,#8fa46a,#b2534c 50%,#4f6a3a)}
.play{position:absolute;left:116px;top:77px;width:38px;height:38px;border-radius:50%;background:rgba(255,255,255,.9)}
.play svg{position:absolute;left:14px;top:11px}
.footer{position:absolute;left:0;top:1072px;width:1037px;height:128px;background:var(--footer)}
.footer-nav{position:absolute;left:82px;top:31px;font-size:12.5px;color:var(--white)}
.footer-nav a{color:var(--white);text-decoration:none}
.footer-nav .sep{margin:0 5px}
.copyright{position:absolute;left:82px;top:60px;font-size:11px;font-weight:300;color:#ddd}
.social{position:absolute;left:879px;top:34px;display:flex;gap:4px}
.social i{width:20px;height:20px;border-radius:3px;background:#3d8fd6}
.social i:last-child{background:#3b5b9e}
</style>
</head>
<body>
<div class="page">
  <header class="header">
    <div class="brand"><span class="brand-mark"></span>brambleridge footcare</div>
    <div class="contact">
      <div class="phone">02 9000 4417</div>
      <div class="address">14 Wattle Lane, Sydney 2000</div>
    </div>
    <div class="search">Search here
      <svg width="15" height="15" viewBox="0 0 15 15"><circle cx="6" cy="6" r="4.8" fill="none" stroke="#aaa" stroke-width="1.5"/><line x1="9.5" y1="9.5" x2="14" y2="14" stroke="#aaa" stroke-width="1.8"/></svg>
    </div>
  </header>
  <nav class="nav">
    <a href="#">Home</a><a href="#">About Us</a><a href="#">What is Planter Fasciitis?</a><a href="#">Treatments</a><a href="#">Planter Fasciitis Treatment</a><a href="#">Contact Us</a>
  </nav>
  <section class="hero">
    <h1>Physcial Therapy and <span>Heel Pain Relief</span></h1>
    <p>Class aptent taciti sociosqu ad litora torquent per conubia nostra, per inceptos hymenaeos. Proin nulla arcu, nonummy luctus, dictum eget, fermentum et, lorem. Nunc porta convallis pede.</p>
    <div class="dots"><i></i><i></i><i></i></div>
    <div class="hero-photo" role="img" aria-label="Therapist's hands massaging a patient's foot resting on a towel"></div>
  </section>

  <article class="card" style="left:86px">
    <h2>Patient Education</h2>
    <div class="photo" role="img" aria-label="Two women stretching in an exercise class" style="background:linear-gradient(120deg,#3f6fa8,#e9e1dc 60%,#c9cdd4)"></div>
    <p>Aliquam nec erat at purus cursus interdum. Vestibulum ligula augue, bibendum accumsan, vestibulum ut, commodo a, mi.</p>
    <a class="more" href="#">LEARN MORE</a>
  </article>
  <article class="card" style="left:380px">
    <h2>Make an Appointment</h2>
    <div class="photo" role="img" aria-label="Physiotherapist treating a patient lying on a treatment table" style="background:linear-gradient(120deg,#d83a3a,#efe4d9 55%,#f3efea)"></div>
    <p>Aliquam nec erat at purus cursus interdum. Vestibulum ligula augue, bibendum accumsan, vestibulum ut, commodo a, mi.</p>
    <a class="more" href="#">LEARN MORE</a>
  </article>
  <article class="card is-active" style="left:673px">
    <h2>Clinic Locations</h2>
    <div class="photo" role="img" aria-label="Smartphone showing a navigation map" style="background:linear-gradient(150deg,#cfd3d6,#e8d98e 45%,#2d6fb8 80%,#222)"></div>
    <p>Aliquam nec erat at purus cursus interdum. Vestibulum ligula augue, bibendum accumsan, vestibulum ut, commodo a, mi.</p>
    <a class="more" href="#">LEARN MORE</a>
  </article>

  <section class="welcome">
    <h2>Welcome to Brambleridge Foot Care Mainpage..</h2>
    <p style="top:874px">Vivamus porttitor, g, purus nisi eleifend libero, a tempus libero lectus feugiat felis. Morbi diam mauris, viverra in, gravida eu, mattis in, ante. Morbi eget arcu. Morbi porta, libero id ullamcorper nonummy, nibh ligula pulvinar metus, eget consectetuer augue nisi quis lacus. Ut ac mi quis lacus mollis aliquam.</p>
    <p style="top:942px">Phasellus felis dolor, scelerisque a, tempus eget, lobortis id, libero. Donec scelerisque leo ac risus. Praesent sit amet est. In dictum, dolor eu dictum porttitor, enim felis viverra mi, eget luctus massa purus quis odio. Etiam nulla massa, pharetra facilisis, volutpat in, imperdiet sit amet, sem. Aliquam nec erat at purus cursus interdum.</p>
    <div class="video" role="img" aria-label="Video of a coach helping a runner stretch her leg outdoors">
      <div class="play"><svg width="12" height="16" viewBox="0 0 12 16"><path d="M0 0L12 8L0 16Z" fill="#111"/></svg></div>
    </div>
  </section>

  <footer class="footer">
    <div class="footer-nav">
      <a href="#">Home</a><span class="sep">|</span><a href="#">About Us</a><span class="sep">|</span><a href="#">What is Planter Fasciitis?</a><span class="sep">|</span><a href="#">Treatments</a><span class="sep">|</span><a href="#">Planter Fasciitis Treatment</a><span class="sep">|</span><a href="#">Contact Us</a>
    </div>
    <div class="copyright">© 2012 Company Name.&nbsp; All right reserved.&nbsp; Term of Use</div>
    <div class="social"><i></i><i></i><i></i></div>
  </footer>
</div>
</body>
</html>
```